" Vendemos planos de saúde para pessoas físicas. Vendemos desde planos bem populares(baratos) como Vivassa até produtos mais sofisticados como Corlanto. Comercializamos também Elvor, Pravime, Terra Nova e Dentrafa (Dentrafa é plano odontológico). "

```html
<!DOCTYPE html>
<html lang="pt-BR">
<head>
<meta charset="utf-8">
<title>Aurevi Corretora de Planos de Saúde</title>
<link rel="stylesheet" href="https://fonts.googleapis.com/css2?family=Cormorant+Garamond:wght@500;600&family=Open+Sans:wght@400;600;700;800&display=swap">
<style>
  :root {
    --navy: #1f3f7a;
    --navy-dark: #15305f;
    --gold: #e3a32a;
    --orange: #f08a1c;
    --ink: #2b2b2b;
    --muted: #7b8190;
    --paper: #ffffff;
    --bg: #ffffff;
    --form-bg: rgba(28, 30, 38, 0.88);
    --photo-a: #c9b8a3;
    --photo-b: #e7ddd0;
    --photo-c: #8fa0b6;
  }
  * { box-sizing: border-box; margin: 0; padding: 0; }
  html, body { width: 1200px; height: 1200px; overflow: hidden; background: var(--bg); }
  body { font-family: "Open Sans", sans-serif; color: var(--ink); position: relative; }

  .brand-mark {
    position: absolute; top: 90px; left: 0; width: 1200px;
    display: flex; flex-direction: column; align-items: center;
  }
  .brand-mark .brand-name {
    font-family: "Cormorant Garamond", serif; font-weight: 600;
    font-size: 92px; letter-spacing: 6px; color: var(--navy); line-height: 1;
    display: flex; align-items: center; gap: 22px;
  }
  .brand-mark .brand-dot { width: 28px; height: 28px; border-radius: 50%; background: var(--gold); }
  .brand-mark .brand-tag {
    font-family: "Open Sans", sans-serif; font-size: 17px; font-weight: 600;
    letter-spacing: 3px; color: var(--navy); margin-top: 10px; text-transform: uppercase;
  }

  .site {
    position: absolute; top: 300px; left: 100px; width: 1000px; height: 860px;
    background: var(--paper); box-shadow: 0 0 0 1px #e3e6ec; overflow: hidden;
  }
  .topbar {
    height: 30px; background: var(--navy-dark);
    display: flex; justify-content: flex-end; align-items: center; gap: 10px; padding-right: 60px;
  }
  .topbar .social { width: 14px; height: 14px; border-radius: 50%; background: #5d77a8; }

  .header {
    height: 88px; display: flex; align-items: center; justify-content: space-between;
    padding: 0 60px; border-bottom: 1px solid #eceef2;
  }
  .header .logo {
    font-family: "Cormorant Garamond", serif; font-weight: 600; font-size: 38px;
    letter-spacing: 3px; color: var(--navy); display: flex; align-items: center; gap: 10px;
  }
  .header .logo .brand-dot { width: 12px; height: 12px; border-radius: 50%; background: var(--gold); }
  .contacts { display: flex; align-items: center; gap: 26px; font-weight: 700; font-size: 18px; color: var(--navy); }
  .contacts .item { display: flex; align-items: center; gap: 8px; }
  .contacts .chat b { color: var(--navy); }
  .contacts .chat span { color: var(--orange); }

  .nav {
    height: 36px; display: flex; align-items: center; gap: 34px; padding: 0 60px;
    font-size: 12px; font-weight: 700; color: var(--orange); letter-spacing: .5px;
    border-bottom: 1px solid #eceef2;
  }
  .nav .active { color: var(--navy); }

  .hero {
    position: relative; height: 410px;
    background: linear-gradient(110deg, var(--photo-b) 0%, var(--photo-a) 45%, var(--photo-c) 100%);
  }
  .hero .slogan {
    position: absolute; left: 0; top: 250px; background: var(--navy);
    color: #fff; font-weight: 800; font-size: 14px; padding: 14px 30px 14px 60px; letter-spacing: .5px;
  }
  .lead-form {
    position: absolute; right: 150px; top: 80px; width: 270px; padding: 22px 22px 26px;
    background: var(--form-bg);
  }
  .lead-form h2 {
    font-size: 14px; font-weight: 800; color: #fff; line-height: 1.25; margin-bottom: 16px;
    display: flex; gap: 10px; align-items: flex-start;
  }
  .lead-form h2 em { font-style: normal; color: var(--gold); }
  .lead-form .field { height: 22px; background: #fff; margin-bottom: 8px; }
  .lead-form .send {
    margin: 14px auto 0; width: 130px; height: 28px; background: var(--navy);
    color: #fff; font-size: 12px; font-weight: 800; display: flex; align-items: center; justify-content: center;
  }
  .lead-form .note { margin-top: 10px; font-size: 9px; color: #9aa0ad; text-align: center; }

  .partners { padding: 36px 60px 0; }
  .partners h3 { font-size: 18px; font-weight: 800; color: var(--navy); margin-bottom: 30px; }
  .partner-row { display: flex; justify-content: space-between; align-items: center; }
  .partner { font-weight: 800; font-size: 26px; }
  .p-vivassa { color: #e2611c; }
  .p-elvor { color: #2a5da8; }
  .p-pravime { color: #fff; background: #0f7a3d; padding: 2px 10px; }
  .p-terra { color: #e0262f; }
  .p-corlanto { color: #c8102e; }
  .p-dentrafa { color: #1b8f6a; }
</style>
</head>
<body>
  <header class="brand-mark">
    <div class="brand-name"><span class="brand-dot"></span>AUREVI</div>
    <div class="brand-tag">Corretora de Planos de Saúde</div>
  </header>

  <main class="site">
    <div class="topbar">
      <span class="social"></span><span class="social"></span><span class="social"></span><span class="social"></span><span class="social"></span>
    </div>

    <div class="header">
      <div class="logo"><span class="brand-dot"></span>AUREVI</div>
      <div class="contacts">
        <div class="item">
          <svg width="20" height="20" viewBox="0 0 24 24"><path fill="#1f3f7a" d="M6.6 10.8a15 15 0 0 0 6.6 6.6l2.2-2.2c.3-.3.7-.4 1-.2 1.1.4 2.3.6 3.6.6.6 0 1 .4 1 1V20c0 .6-.4 1-1 1A17 17 0 0 1 3 4c0-.6.4-1 1-1h3.5c.6 0 1 .4 1 1 0 1.3.2 2.5.6 3.6.1.3 0 .7-.2 1z"/></svg>
          (81) 3555-0142
        </div>
        <div class="item chat">
          <svg width="22" height="20" viewBox="0 0 24 22"><path fill="#1f3f7a" d="M3 2h18a1 1 0 0 1 1 1v12a1 1 0 0 1-1 1H9l-5 4v-4H3a1 1 0 0 1-1-1V3a1 1 0 0 1 1-1z"/></svg>
          <b>CHAT</b><span>ONLINE</span>
        </div>
      </div>
    </div>

    <nav class="nav">
      <span class="active">SOLICITE SEU ORÇAMENTO</span>
      <span>EMPRESA</span><span>PLANOS</span><span>CONTATO</span><span>VANTAGENS</span><span>DÚVIDAS</span><span>BLOG</span>
    </nav>

    <section class="hero" role="img" aria-label="Foto de uma família sorridente ao ar livre">
      <div class="slogan">SAÚDE É TUDO, E PREÇO BAIXO TAMBÉM!</div>
      <form class="lead-form">
        <h2>
          <svg width="26" height="22" viewBox="0 0 26 22"><rect x="1" y="2" width="14" height="10" fill="#fff"/><rect x="10" y="8" width="14" height="10" fill="#c9d3e6"/></svg>
          <span>CONVERSE COM<br>NOSSOS <em>CORRETORES</em></span>
        </h2>
        <div class="field"></div>
        <div class="field"></div>
        <div class="field"></div>
        <div class="send">ENVIAR</div>
        <div class="note">Retornamos seu contato em breve</div>
      </form>
    </section>

    <section class="partners">
      <h3>PLANOS DE SAÚDE PARCEIROS</h3>
      <div class="partner-row">
        <span class="partner p-vivassa">Vivassa</span>
        <span class="partner p-elvor">Elvor</span>
        <span class="partner p-pravime">Pravime</span>
        <span class="partner p-terra">Terra Nova</span>
        <span class="partner p-corlanto">Corlanto</span>
        <span class="partner p-dentrafa">Dentrafa</span>
      </div>
    </section>
  </main>
</body>
</html>
```